Design a clean professional business card with debossed front design. Front of the business car to include the provided vertical logo and creatively displayed service offerings at the bottom of the card to include Development Services, Engineering, Asset Management.
You can reference the design link to the website that is in the final stages of completion for color and style.
https://q42.77k.brightstagehost.net
Back side of card:
The back of the card is to include the provided horizontal logo at the top left corner. Please include a QR code that links to the website (www.norquillbuild.com) in the top right area of the card. Please include the following information:
Name
Title
Mobile #
Office #
Email
Website (www.norquillbuild.com)
Address
418 W. 9th Ave, Ferndale, CO 80214
Target Market(s)
Construction, engineering, development, architecture
Industry/Entity Type
Contact Information for Business Card
See description
Look and feel
Each slider illustrates characteristics of the customer's brand and the style your logo design should communicate.

```html
<!DOCTYPE html>
<html lang="en">
<head>
<meta charset="utf-8">
<title>Norquill Build – Business Card</title>
<link rel="stylesheet" href="https://fonts.googleapis.com/css2?family=Montserrat:wght@300;400;600;700&display=swap">
<style>
  :root {
    --stage: #1f2c53;
    --navy: #1f2c53;
    --amber: #e8a317;
    --ochre: #b8730a;
    --ink: #2b2118;
    --paper: #ececea;
    --grey: #5a5a5a;
    --qr-tone: #c9c9c6;
  }
  * { box-sizing: border-box; margin: 0; padding: 0; }
  html, body { width: 1200px; height: 960px; overflow: hidden; }
  body {
    background: var(--stage);
    font-family: "Montserrat", sans-serif;
    display: flex;
    align-items: center;
    justify-content: center;
    gap: 40px;
  }
  .card {
    width: 540px;
    height: 309px;
    position: relative;
    border-radius: 2px;
    overflow: hidden;
  }

  /* Back side */
  .card--back { background: var(--paper); color: var(--navy); }
  .brand-lockup { position: absolute; left: 36px; top: 34px; }
  .brand-lockup__row { display: flex; align-items: center; gap: 10px; }
  .brand-lockup__square { width: 22px; height: 22px; background: var(--navy); }
  .brand-lockup__name { font-weight: 600; font-size: 22px; letter-spacing: 2px; }
  .brand-lockup__tagline {
    font-size: 7px; font-weight: 600; letter-spacing: 1.6px;
    text-transform: uppercase; margin-top: 4px; margin-left: 32px;
  }
  .qr-code {
    position: absolute; right: 36px; top: 30px;
    width: 84px; height: 84px; background: var(--qr-tone);
  }
  .person { position: absolute; left: 36px; top: 128px; }
  .person__name { font-size: 17px; letter-spacing: 1.5px; text-transform: uppercase; }
  .person__first { font-weight: 700; }
  .person__last { font-weight: 300; color: var(--amber); }
  .person__title { font-size: 13px; font-weight: 300; color: var(--amber); }
  .divider {
    position: absolute; left: 36px; top: 180px; width: 260px;
    height: 1px; background: var(--amber);
  }
  .contact-list {
    position: absolute; left: 36px; top: 190px; list-style: none;
    font-size: 12px; color: var(--grey); letter-spacing: 1px; line-height: 19px;
  }
  .contact-list li { display: flex; align-items: center; gap: 8px; }
  .contact-list svg { width: 12px; height: 12px; fill: var(--navy); flex: none; }

  /* Front side */
  .card--front {
    background: var(--ochre); color: var(--ink);
    display: flex; flex-direction: column; align-items: center;
  }
  .front-lockup {
    margin-top: 52px; text-align: center;
    display: flex; flex-direction: column; align-items: center;
  }
  .front-lockup__square { width: 56px; height: 56px; background: var(--ink); margin-bottom: 16px; }
  .front-lockup__name { font-size: 44px; font-weight: 600; letter-spacing: 4px; line-height: 1; }
  .front-lockup__tagline {
    font-size: 10px; font-weight: 600; letter-spacing: 3px;
    text-transform: uppercase; margin-top: 8px;
  }
  .services {
    position: absolute; bottom: 26px; left: 0; right: 0; text-align: center;
    font-size: 12px; font-weight: 700; letter-spacing: 1.6px; text-transform: uppercase;
  }
</style>
</head>
<body>

  <section class="card card--back" aria-label="Card back">
    <div class="brand-lockup">
      <div class="brand-lockup__row">
        <span class="brand-lockup__square"></span>
        <span class="brand-lockup__name">NORQUILL BUILD</span>
      </div>
      <p class="brand-lockup__tagline">Trusted Partners - Timely Service</p>
    </div>

    <div class="qr-code" role="img" aria-label="QR code linking to www.norquillbuild.com"></div>

    <div class="person">
      <p class="person__name"><span class="person__first">Person</span> <span class="person__last">Name</span></p>
      <p class="person__title">Title</p>
    </div>

    <div class="divider"></div>

    <ul class="contact-list">
      <li><svg viewBox="0 0 24 24"><path d="M6.6 10.8a15 15 0 0 0 6.6 6.6l2.2-2.2a1 1 0 0 1 1-.25 11.4 11.4 0 0 0 3.6.57 1 1 0 0 1 1 1V20a1 1 0 0 1-1 1A17 17 0 0 1 3 4a1 1 0 0 1 1-1h3.5a1 1 0 0 1 1 1c0 1.25.2 2.45.57 3.6a1 1 0 0 1-.25 1z"/></svg>M# 005 4321 876</li>
      <li><svg viewBox="0 0 24 24"><path d="M4 8h16v12H4z M7 3h10v4H7z"/></svg>O# 003 98765 412</li>
      <li><svg viewBox="0 0 24 24"><path d="M2 5h20v14H2zm2 2v.5l8 5 8-5V7z"/></svg>info@norquillbuild.com</li>
      <li><svg viewBox="0 0 24 24"><path d="M12 2a10 10 0 1 0 0 20 10 10 0 0 0 0-20zm0 2.2a7.8 7.8 0 1 1 0 15.6 7.8 7.8 0 0 1 0-15.6z"/></svg>www.norquillbuild.com</li>
      <li><svg viewBox="0 0 24 24"><path d="M12 2a7 7 0 0 0-7 7c0 5 7 13 7 13s7-8 7-13a7 7 0 0 0-7-7zm0 9.5a2.5 2.5 0 1 1 0-5 2.5 2.5 0 0 1 0 5z"/></svg>418 W. 9th Ave, Ferndale, CO 80214</li>
    </ul>
  </section>

  <section class="card card--front" aria-label="Card front">
    <div class="front-lockup">
      <span class="front-lockup__square"></span>
      <p class="front-lockup__name">NORQUILL BUILD</p>
      <p class="front-lockup__tagline">Trusted Partners - Timely Service</p>
    </div>
    <p class="services">Development Services - Engineering - Asset Management</p>
  </section>

</body>
</html>
```